New business card design for Pinecrest Hollow Optometry Clinic

We need a new business card design using our existing logo (uploaded). Please do not include eyes, eye exam charts or beaches, water, sand. The logo I uploaded shows our colors of green and blue, but we are open to seeing it in black OR white. We would like to see something modern and fresh. It will need to be 2 sided. On the front we will need to be able to put a doctors name, for example-Dr Marta Kellerman and Associates. We will need to be able to change the name to other doctors names when we send for printing. The back of the card should list the following: 3817 Tarrow St, Fenmoor Bay (P)705-555-0148 (E) info@phoc.ca www.phoc.ca. "We are welcoming new patients" and a line for the appointment date and time. I have uploaded the back of a card to give an example

```html
<!DOCTYPE html>
<html lang="en">
<head>
<meta charset="utf-8">
<title>Pinecrest Hollow Optometry Clinic – Business Card</title>
<link href="https://fonts.googleapis.com/css2?family=Source+Sans+3:wght@400;600&display=swap" rel="stylesheet">
<style>
  :root {
    --backdrop: #d2d3d5;
    --teal: #05b1ab;
    --teal-light: #72dcd5;
    --white: #ffffff;
    --ink: #111111;
    --ink-soft: #222222;
  }
  html, body {
    margin: 0;
    padding: 0;
    width: 1200px;
    height: 1200px;
    overflow: hidden;
    background: var(--backdrop);
    font-family: "Source Sans 3", "Myriad Pro", sans-serif;
  }
  .card {
    position: absolute;
    left: 276px;
    width: 648px;
    height: 390px;
    border-radius: 25px;
    overflow: hidden;
    background: var(--white);
  }
  .card svg { display: block; width: 100%; height: 100%; }
  .card--front { top: 125px; }
  .card--back { top: 621px; }
  .fill-teal { fill: var(--teal); }
  .fill-teal-light { fill: var(--teal-light); }
  .stroke-white { stroke: var(--white); fill: none; }
  .stroke-teal { stroke: var(--teal); fill: none; }
  .brand-name { fill: var(--ink); font-weight: 600; }
  .clinic-name { fill: var(--ink); font-weight: 400; }
  .doctor-name { fill: var(--white); font-weight: 600; }
  .welcome { fill: var(--white); font-weight: 400; }
  .field-label { fill: var(--white); font-weight: 400; }
  .field-line { stroke: var(--white); stroke-width: 1.5; }
  .contact-ring { fill: none; stroke: var(--ink); stroke-width: 1.6; }
  .contact-icon { fill: var(--teal); }
  .contact-text { fill: var(--ink-soft); font-weight: 400; }
</style>
</head>
<body>

<!-- Front side -->
<div class="card card--front">
  <svg viewBox="0 0 1043 627" xmlns="http://www.w3.org/2000/svg">
    <path class="fill-teal-light" d="M428,180 Q408,205 418,235 L503,627 H600 Z"/>
    <path class="fill-teal" d="M581,0 H1043 V627 H561 L426,258 Q410,215 440,178 Z"/>
    <path class="stroke-white" stroke-width="14" d="M680,0 L522,188 Q508,208 516,232 L652,627"/>
    <line class="stroke-white" stroke-width="2" x1="689" y1="0" x2="689" y2="627"/>
    <text class="brand-name" x="96" y="421" font-size="305" textLength="850" lengthAdjust="spacingAndGlyphs">PHOC</text>
    <text class="clinic-name" x="100" y="507" font-size="64" textLength="852" lengthAdjust="spacingAndGlyphs">Pinecrest Hollow Optometry Clinic</text>
  </svg>
</div>

<!-- Back side -->
<div class="card card--back">
  <svg viewBox="0 0 1044 627" xmlns="http://www.w3.org/2000/svg">
    <path class="fill-teal-light" d="M628,268 Q662,305 650,348 L568,627 H520 Z"/>
    <path class="fill-teal" d="M0,0 H501 L633,190 Q646,212 638,238 L520,627 H0 Z"/>
    <path class="stroke-teal" stroke-width="14" d="M583,0 L710,188 Q726,214 718,242 L606,627"/>

    <text class="doctor-name" x="73" y="140" font-size="37" textLength="496" lengthAdjust="spacingAndGlyphs">Dr Marta Kellerman &amp; Associates</text>
    <line class="field-line" x1="73" y1="153" x2="569" y2="153"/>
    <text class="welcome" x="71" y="217" font-size="32">We are welcoming new patients!</text>

    <text class="field-label" x="73" y="310" font-size="24">Doctor:</text>
    <line class="field-line" x1="160" y1="310" x2="578" y2="310"/>
    <text class="field-label" x="74" y="404" font-size="24">Date:</text>
    <line class="field-line" x1="134" y1="403" x2="356" y2="403"/>
    <text class="field-label" x="69" y="499" font-size="24">Time:</text>
    <line class="field-line" x1="135" y1="498" x2="357" y2="498"/>

    <text class="brand-name" x="878" y="175" font-size="72" text-anchor="middle">PHOC</text>

    <g class="contact">
      <circle class="contact-ring" cx="773" cy="373" r="26"/>
      <path class="contact-icon" d="M764,362 q3,-3 6,0 l3,4 q1,3 -1,5 l-2,2 q3,6 9,9 l2,-2 q2,-2 5,-1 l4,3 q3,3 0,6 l-2,2 q-4,3 -12,-2 q-8,-6 -13,-14 q-3,-7 1,-12 z"/>
      <text class="contact-text" x="813" y="383" font-size="22">705-555-0148</text>
    </g>
    <g class="contact">
      <circle class="contact-ring" cx="773" cy="433" r="26"/>
      <rect class="contact-icon" x="761" y="425" width="24" height="16" rx="1"/>
      <polyline points="761,426 773,435 785,426" fill="none" stroke="#fff" stroke-width="1.6"/>
      <text class="contact-text" x="815" y="442" font-size="22">info@phoc.ca</text>
    </g>
    <g class="contact">
      <circle class="contact-ring" cx="773" cy="493" r="26"/>
      <path class="contact-icon" d="M767,481 L782,494 L775,495 L779,504 L776,505 L772,497 L767,501 Z"/>
      <text class="contact-text" x="813" y="498" font-size="22">www.phoc.ca.</text>
    </g>
    <g class="contact">
      <circle class="contact-ring" cx="773" cy="553" r="26"/>
      <path class="contact-icon" d="M773,567 Q763,553 763,547 A10,10 0 0 1 783,547 Q783,553 773,567 Z"/>
      <circle cx="773" cy="547" r="3.5" fill="#fff"/>
      <text class="contact-text" x="814" y="550" font-size="22">3817 Tarrow St,</text>
      <text class="contact-text" x="814" y="578" font-size="22">Fenmoor Bay</text>
    </g>
  </svg>
</div>

</body>
</html>
```